Business Card Design

chiropractor. Searching for a fresh cool look. Tired of all the run of the mill designs. I am open tocolors and all new designs..

Target Market(s)

auto accidents workers compensation and private insurance

Industry/Entity Type

Business

Contact Information for Business Card

Dr. Mark S. Snyder193-02 northern blvd.Flushing, new york 11358Upper level rear suitephone 718 224 3605fax 718 555 0187

Font styles to use
Sans Serif

Requirements
Must have
• my office hours on back of card
• monday 9am-noon; 2:30pm-7pm
• tuesday 2:30pm-7pm
• wednesday 9am-noon; 2;30pm-7pm
• thursday 4pm-7pm
• friday4pm-7pm
Nice to have
• some kind of real cool logo

```html
<!DOCTYPE html>
<html lang="en">
<head>
<meta charset="utf-8">
<title>Chiropractic Clinic – Business Card</title>
<link href="https://fonts.googleapis.com/css2?family=Alegreya+Sans:wght@400;500;700&display=swap" rel="stylesheet">
<style>
  :root {
    --stage: #2f3d44;
    --teal: #0b7185;
    --teal-text: #0d7388;
    --paper: #ffffff;
    --ink: #1f1f1f;
    --on-teal: #ffffff;
    --rule: rgba(255,255,255,0.55);
  }
  * { margin: 0; padding: 0; box-sizing: border-box; }
  html, body {
    width: 1200px; height: 1000px; overflow: hidden;
    background: var(--stage);
    font-family: "Alegreya Sans", "Helvetica Neue", Arial, sans-serif;
  }
  .stage {
    width: 1200px; height: 1000px;
    display: flex; flex-direction: column; align-items: center; justify-content: center;
    gap: 50px;
  }
  .card {
    position: relative;
    width: 740px; height: 423px;
    box-shadow: 0 10px 30px rgba(0,0,0,0.35);
  }

  /* Back side: office hours */
  .card--back { background: var(--teal); color: var(--on-teal); }
  .hours {
    position: absolute; left: 190px; top: 82px; width: 370px;
  }
  .hours__title {
    font-weight: 700; font-size: 19px; letter-spacing: 0.2px;
    padding-left: 30px; margin-bottom: 6px;
  }
  .hours__rule {
    border-top: 1px dotted var(--rule); margin-bottom: 8px;
  }
  .hours__table { border-collapse: collapse; margin-left: 26px; font-size: 17px; }
  .hours__table td { padding: 0; line-height: 20px; vertical-align: top; }
  .hours__day { width: 128px; }

  /* Front side: identity and contact */
  .card--front { background: var(--paper); color: var(--ink); }
  .identity {
    position: absolute; right: 82px; top: 68px; text-align: right;
  }
  .identity__clinic { font-size: 37px; font-weight: 400; letter-spacing: 0.3px; line-height: 1; }
  .identity__tagline { font-size: 22px; color: var(--teal-text); margin-top: 6px; }
  .doctor {
    position: absolute; right: 102px; top: 176px;
    font-size: 24px; font-weight: 700;
  }
  .contacts {
    position: absolute; right: 68px; top: 268px;
    list-style: none; text-align: right;
  }
  .contacts__item {
    display: flex; justify-content: flex-end; align-items: center;
    font-size: 23px; height: 40px; gap: 10px;
  }
  .contacts__icon {
    width: 30px; height: 30px; background: var(--teal);
    display: inline-flex; align-items: center; justify-content: center;
  }
  .contacts__icon svg { width: 18px; height: 18px; fill: var(--on-teal); }
</style>
</head>
<body>
<main class="stage">
  <section class="card card--back" aria-label="Card back: office hours">
    <div class="hours">
      <h2 class="hours__title">Operation Hours</h2>
      <div class="hours__rule"></div>
      <table class="hours__table">
        <tr><td class="hours__day">Monday</td><td>9am-noon; 2:30pm-7pm</td></tr>
        <tr><td class="hours__day">Tuesday</td><td>2:30pm-7pm</td></tr>
        <tr><td class="hours__day">Wednesday</td><td>9am-noon; 2:30pm-7pm</td></tr>
        <tr><td class="hours__day">Thursday</td><td>4pm-7pm</td></tr>
        <tr><td class="hours__day">Friday</td><td>4pm-7pm</td></tr>
      </table>
    </div>
  </section>

  <section class="card card--front" aria-label="Card front: clinic and contact">
    <div class="identity">
      <h1 class="identity__clinic">Chiropractic Clinic</h1>
      <p class="identity__tagline">Better Spine | Better Health</p>
    </div>
    <p class="doctor">Dr. Paul T. Wexley</p>
    <ul class="contacts">
      <li class="contacts__item">
        <span>(718) 555-0142</span>
        <span class="contacts__icon"><svg viewBox="0 0 24 24" aria-hidden="true"><path d="M6.6 10.8a15.1 15.1 0 0 0 6.6 6.6l2.2-2.2c.3-.3.7-.4 1-.2 1.1.4 2.3.6 3.6.6.6 0 1 .4 1 1V20c0 .6-.4 1-1 1A17 17 0 0 1 3 4c0-.6.4-1 1-1h3.5c.6 0 1 .4 1 1 0 1.3.2 2.5.6 3.6.1.3 0 .7-.2 1z"/></svg></span>
      </li>
      <li class="contacts__item">
        <span>(718) 555-0187</span>
        <span class="contacts__icon"><svg viewBox="0 0 24 24" aria-hidden="true"><path d="M7 2h8v5H7zM5 8h14a2 2 0 0 1 2 2v10a2 2 0 0 1-2 2H5a2 2 0 0 1-2-2V10a2 2 0 0 1 2-2zm3 3v3h8v-3zm0 5v2h2v-2zm3 0v2h2v-2zm3 0v2h2v-2z"/></svg></span>
      </li>
      <li class="contacts__item">
        <span>287-14, Hollis Ridge Rd. Flushing, NY 11472</span>
        <span class="contacts__icon"><svg viewBox="0 0 24 24" aria-hidden="true"><path d="M12 2a7 7 0 0 0-7 7c0 5.2 7 13 7 13s7-7.8 7-13a7 7 0 0 0-7-7zm0 9.5A2.5 2.5 0 1 1 12 6.5a2.5 2.5 0 0 1 0 5z"/></svg></span>
      </li>
    </ul>
  </section>
</main>
</body>
</html>
```